tilebaron.org needs a cool website!

I need a website designed for a commercial flooring maintenance company based in Texas. We will be providing services like carpet shampooing, burnishing, resurfacing and power washing. It needs to be cool and trendy.

I’ll need 10-20 pages. I need help deciding on the style and color palette. We will need great stock pictures of different flooring types and you will need to photo shop our logo on imaginary cars or storefronts.

Please have similar experience and an open mind. I’m looking for a partnership and someone to turn to for future projects and upkeep.

The domain is currently hosted on Wix. You will need the ability to develop and code it there.
Updates

Target Market(s)

Commercial businesses and properties

Industry/Entity Type

Floor care

Coding

Coded - Design and coding required

Number of Pages Required

5+ page

Requirements
Must have
• Great pictures of different types of floors.

```html
<!DOCTYPE html>
<html lang="en">
<head>
<meta charset="utf-8">
<title>Tile Baron – Commercial Floor Care</title>
<link href="https://fonts.googleapis.com/css2?family=Poppins:wght@500;600;700;800&family=Montserrat:wght@400;500;600;700&display=swap" rel="stylesheet">
<style>
:root{
  --navy:#073a6a;
  --ink:#111111;
  --text:#333333;
  --muted:#666666;
  --sage:#eef1df;
  --sage-dark:#e3e8cf;
  --white:#ffffff;
  --map:#d8f5e4;
}
*{margin:0;padding:0;box-sizing:border-box}
html,body{width:1200px;height:3992px;overflow:hidden}
body{position:relative;background:var(--white);font-family:'Montserrat',sans-serif;color:var(--text)}
.abs{position:absolute}
.btn{position:absolute;display:flex;align-items:center;justify-content:center;background:var(--navy);color:var(--white);font-family:'Montserrat',sans-serif;font-weight:700;font-size:16px;border-radius:24px;text-decoration:none}
h1,h2,h3{font-family:'Poppins',sans-serif;color:var(--ink)}

/* header */
.site-header{position:absolute;left:0;top:0;width:1200px;height:84px;background:var(--white)}
.brand{position:absolute;left:113px;top:20px;display:flex;align-items:center;gap:10px;font-family:'Montserrat',sans-serif;font-weight:500;font-size:32px;color:var(--ink)}
.brand-dot{width:16px;height:16px;border-radius:50%;background:var(--navy)}
.nav a{position:absolute;top:33px;font-size:12.5px;font-weight:600;color:var(--ink);text-decoration:none}
.nav a.active{color:var(--navy);text-decoration:underline;text-underline-offset:5px}
.cta-top{left:912px;top:17px;width:171px;height:47px}

/* hero */
.hero{position:absolute;left:0;top:84px;width:1200px;height:557px;background:linear-gradient(100deg,#0d3a68 0%,#1c4f80 40%,#5b7a8f 70%,#8c8d6e 100%)}
.hero-kicker{position:absolute;left:110px;top:118px;color:var(--white);font-family:'Montserrat',sans-serif;font-weight:500;font-size:26px}
.hero-title{position:absolute;left:108px;top:150px;color:var(--white);font-family:'Poppins',sans-serif;font-weight:800;font-size:70px;letter-spacing:1px;line-height:1}
.hero-sub{position:absolute;left:110px;top:239px;color:var(--white);font-weight:700;font-size:17.5px;line-height:30px}
.hero-btn{position:absolute;left:113px;top:320px;width:171px;height:46px;border:2px solid var(--white);border-radius:24px;color:var(--white);display:flex;align-items:center;justify-content:center;font-weight:700;font-size:16px}

/* about */
.about-photo{position:absolute;left:0;top:641px;width:599px;height:509px;background:linear-gradient(180deg,#4f86c4 0%,#9fb6cf 40%,#8d949e 65%,#55604f 100%)}
.section-title{font-family:'Poppins',sans-serif;font-weight:600;font-size:38px;color:var(--ink);line-height:1.2}
.para{font-size:14.5px;line-height:29px;color:var(--text)}

/* services */
.services{position:absolute;left:0;top:1150px;width:1200px;height:763px;background:var(--sage)}
.card{position:absolute;background:var(--white);box-shadow:0 2px 8px rgba(0,0,0,.08)}
.service-card{top:170px;width:303px;height:412px;text-align:center}
.icon-circle{position:absolute;left:98px;top:45px;width:106px;height:106px;border-radius:50%;background:var(--sage)}
.service-card h3{position:absolute;left:0;width:100%;top:178px;font-weight:600;font-size:22px}
.service-card p{position:absolute;left:18px;width:267px;top:228px;font-size:14.5px;line-height:29px;color:var(--muted)}
.service-card .btn{left:66px;top:337px;width:171px;height:46px}

/* commercial */
.van-photo{position:absolute;left:600px;top:1913px;width:600px;height:511px;background:linear-gradient(120deg,#6b4a33 0%,#c89a6b 35%,#d8d7d2 55%,#5d6168 100%)}

/* news */
.news{position:absolute;left:0;top:2424px;width:1200px;height:1048px;background:var(--sage)}
.news-card{top:159px;width:303px;height:405px}
.news-img{position:absolute;left:8px;top:6px;width:287px;height:186px}
.news-card h3{position:absolute;left:21px;top:217px;width:265px;font-weight:600;font-size:19.5px;line-height:27px}
.news-date{position:absolute;left:21px;top:280px;display:flex;align-items:center;gap:8px;font-size:13.5px;font-weight:600;color:var(--ink)}
.news-card p{position:absolute;left:21px;top:306px;width:230px;font-size:14px;line-height:28px}
.read-more{position:absolute;left:21px;top:370px;font-size:13.5px;font-weight:700;color:var(--ink);text-decoration:underline}

/* contact */
.map{position:absolute;left:0;top:3472px;width:1200px;height:440px;background:var(--map)}
.contact-form{position:absolute;left:110px;top:3183px;width:518px;height:470px;background:var(--white)}
.field{position:absolute;border-bottom:1.5px solid #555;font-size:14px;color:var(--text);padding-bottom:9px}
.contact-info{position:absolute;left:628px;top:3183px;width:460px;height:470px;background:var(--navy);color:var(--white);font-size:14.5px}
.contact-info .t{position:absolute;left:40px}
.site-footer{position:absolute;left:0;top:3912px;width:1200px;height:80px;background:var(--navy);color:var(--white);font-size:14px;display:flex;align-items:center;justify-content:center}
</style>
</head>
<body>

<header class="site-header">
  <div class="brand"><span class="brand-dot"></span>tilebaron.org</div>
  <nav class="nav">
    <a class="active" style="left:418px">HOME</a>
    <a style="left:505px">ABOUT</a>
    <a style="left:593px">ARTICLES</a>
    <a style="left:697px">SERVICES</a>
    <a style="left:800px">CONTACT US</a>
  </nav>
  <a class="btn cta-top">Get In Touch</a>
</header>

<section class="hero" role="img" aria-label="Power washer spraying a glossy warehouse floor">
  <div class="hero-kicker">WELCOME TO</div>
  <div class="hero-title">TILE BARON</div>
  <div class="hero-sub">Carpet Shampooing, Burnishing, Resurfacing<br>And Power Washing</div>
  <div class="hero-btn">Get Started</div>
</section>

<section>
  <div class="about-photo" role="img" aria-label="Modern grey commercial building under a blue sky"></div>
  <h2 class="section-title abs" style="left:624px;top:722px">ABOUT US</h2>
  <p class="para abs" style="left:627px;top:782px;width:420px">Lorem Ipsum is simply dummy text of the printing and typesetting industry. Lorem Ipsum has been the industry's standard dummy text ever since the 1500s, when an unknown printer took a galley of type and scrambled it to make a type specimen book. It has survived not only five centuries, but also the leap into electronic typesetting, remaining essentially</p>
  <a class="btn" style="left:628px;top:1015px;width:171px;height:47px">Learn More</a>
</section>

<section class="services">
  <h2 class="section-title abs" style="left:0;width:1200px;text-align:center;top:88px">DISCOVER OUR SERVICES</h2>

  <div class="card service-card" style="left:110px">
    <div class="icon-circle">
      <svg width="106" height="106" viewBox="0 0 106 106" fill="none" stroke="#222" stroke-width="2"><rect x="32" y="34" width="26" height="38" rx="3"/><circle cx="40" cy="62" r="5"/><rect x="60" y="44" width="14" height="28" rx="2"/><path d="M64 44v-6h6"/></svg>
    </div>
    <h3>Carpet Shampooing</h3>
    <p>Lorem Ipsum is simply dummy text of the printing and typesetting industry. Lorem Ipsum has been the</p>
    <a class="btn">Learn More</a>
  </div>

  <div class="card service-card" style="left:445px">
    <div class="icon-circle">
      <svg width="106" height="106" viewBox="0 0 106 106" fill="none" stroke="#222" stroke-width="2"><rect x="30" y="36" width="46" height="20" rx="6"/><rect x="34" y="58" width="38" height="12"/><path d="M40 58v12M46 58v12M52 58v12M58 58v12M64 58v12"/><circle cx="42" cy="46" r="4"/></svg>
    </div>
    <h3>Burnishing</h3>
    <p>Lorem Ipsum is simply dummy text of the printing and typesetting industry. Lorem Ipsum has been the</p>
    <a class="btn">Learn More</a>
  </div>

  <div class="card service-card" style="left:785px">
    <div class="icon-circle">
      <svg width="106" height="106" viewBox="0 0 106 106" fill="none" stroke="#222" stroke-width="2"><rect x="60" y="34" width="12" height="26" rx="3"/><path d="M60 44L38 64M30 72h36"/><path d="M36 64l-6 8h12z"/></svg>
    </div>
    <h3>Power Washing</h3>
    <p>Lorem Ipsum is simply dummy text of the printing and typesetting industry. Lorem Ipsum has been the</p>
    <a class="btn">Learn More</a>
  </div>

  <a class="btn" style="left:510px;top:628px;width:171px;height:46px">View More</a>
</section>

<section>
  <h2 class="section-title abs" style="left:109px;top:2005px;line-height:47px">COMMERCIAL<br>FLOORING<br>MAINTENANCE</h2>
  <p class="para abs" style="left:113px;top:2162px;width:420px">Lorem Ipsum is simply dummy text of the printing and typesetting industry. Lorem Ipsum has been the industry's standard dummy text ever since the 1500s, when an unknown printer took a galley of type and</p>
  <a class="btn" style="left:114px;top:2298px;width:171px;height:46px">Learn More</a>
  <div class="van-photo" role="img" aria-label="White company service van parked beside a brick building"></div>
</section>

<section class="news">
  <h2 class="section-title abs" style="left:0;width:1200px;text-align:center;top:78px">LATEST NEWS</h2>

  <article class="card news-card" style="left:110px">
    <div class="news-img" role="img" aria-label="Worker power washing a tiled walkway" style="background:linear-gradient(180deg,#6b6f70,#b7bcbb 60%,#8c9292)"></div>
    <h3>Lorem Ipsum is simply dummy text of the</h3>
    <div class="news-date"><svg width="15" height="15" viewBox="0 0 15 15" fill="none" stroke="#222" stroke-width="1.4"><rect x="1" y="2.5" width="13" height="11.5" rx="1.5"/><path d="M1 6h13M4.5 1v3M10.5 1v3"/></svg>March 30,2023</div>
    <p>Lorem Ipsum is simply dummy text of the printing</p>
    <a class="read-more">Read More...</a>
  </article>

  <article class="card news-card" style="left:446px">
    <div class="news-img" role="img" aria-label="Pressure washer cleaning stone steps" style="background:linear-gradient(180deg,#3b4b5c,#7f97a8 55%,#2d86c4)"></div>
    <h3>Lorem Ipsum is simply dummy text of the</h3>
    <div class="news-date"><svg width="15" height="15" viewBox="0 0 15 15" fill="none" stroke="#222" stroke-width="1.4"><rect x="1" y="2.5" width="13" height="11.5" rx="1.5"/><path d="M1 6h13M4.5 1v3M10.5 1v3"/></svg>March 30,2023</div>
    <p>Lorem Ipsum is simply dummy text of the printing</p>
    <a class="read-more">Read More...</a>
  </article>

  <article class="card news-card" style="left:784px">
    <div class="news-img" role="img" aria-label="Worker washing a storefront facade" style="background:linear-gradient(100deg,#cfd2d2,#7b7f80 50%,#2c2f31)"></div>
    <h3>Lorem Ipsum is simply dummy text of the</h3>
    <div class="news-date"><svg width="15" height="15" viewBox="0 0 15 15" fill="none" stroke="#222" stroke-width="1.4"><rect x="1" y="2.5" width="13" height="11.5" rx="1.5"/><path d="M1 6h13M4.5 1v3M10.5 1v3"/></svg>March 30,2023</div>
    <p>Lorem Ipsum is simply dummy text of the printing</p>
    <a class="read-more">Read More...</a>
  </article>

  <a class="btn" style="left:513px;top:618px;width:170px;height:46px">Learn More</a>
</section>

<section>
  <div class="map" role="img" aria-label="Street map of the service area"></div>

  <div class="contact-form">
    <h2 class="section-title abs" style="left:30px;top:42px;font-size:34px">CONTACT US</h2>
    <div class="field" style="left:38px;top:110px;width:217px">Your Name</div>
    <div class="field" style="left:275px;top:110px;width:217px">Email</div>
    <div class="field" style="left:38px;top:174px;width:452px">Phone</div>
    <div class="field" style="left:38px;top:246px;width:452px;height:74px">Your Message</div>
    <a class="btn" style="left:177px;top:355px;width:171px;height:46px">Submit</a>
  </div>

  <div class="contact-info">
    <div class="t" style="top:58px;font-weight:700;font-size:16px">Opening Hours</div>
    <div class="t" style="top:113px">Monday-Friday: 9am to 7pm</div>
    <div class="t" style="top:143px">Saturday: 9am to 4pm</div>
    <div class="t" style="top:173px">Sunday: Closed</div>
    <div class="abs" style="left:40px;top:227px;width:397px;height:1.5px;background:#fff"></div>
    <div class="t" style="left:46px;top:247px;font-weight:700;font-size:13.5px">Call Us</div>
    <div class="t" style="left:46px;top:275px;font-size:13.5px">+1 555 014 2290</div>
    <div class="t" style="left:46px;top:303px;font-weight:700;font-size:13.5px">Mail Us</div>
    <div class="t" style="left:46px;top:331px;font-size:13.5px">info@tilebaron.org</div>
    <div class="t" style="left:46px;top:360px;font-weight:700;font-size:13.5px">Location</div>
    <div class="t" style="left:46px;top:388px;font-size:13.5px">Lorem Ipsum Lorem Ipsum Lorem</div>
  </div>
</section>

<footer class="site-footer">Copyright © 2024&nbsp; Tile Baron | All Rights Reserved</footer>

</body>
</html>
```